Web Design Project for DJ

We need a web design for a DJ. Our client is a freelance DJ who already has a regular gig at a major night club but is looking to expand his exposure. He is located in a major metropolitan area and is looking for further gigs. He is hoping to generate further business via the website, including bookings via the site.

For reference his pagelinker page is here https://www.pagelinker.example/pages/DJ-Vorn/730162948415207

Following face to face discussions with the client today we have made a few small alterations to the brief.  We are hoping to have some images uploaded shortly.

Target Market(s)

Event planners, night club owners, radio stations, younger age groups (16-35)

Industry/Entity Type

Business

Requirements
Must have
• Name is DJVorn, this should obviously feature prominently. His current business card is attached as an example.

Links to Pagelinker and Tunedrift

Cool, modern look, slightly edgy.

Site will be built in Joomla, so a front page and secondary page template is required.
Nice to have
• Blog style layout to front page featuring recent and upcoming gigs.

Secondary pages may include a more expansive blog, a list of upcoming gigs, and a booking form.

Darker colour palettes preferred and use of same/similar fonts to those on the business card are an obvious plus

```html
<!DOCTYPE html>
<html lang="en">
<head>
<meta charset="utf-8">
<title>DJVorn</title>
<link rel="stylesheet" href="https://fonts.googleapis.com/css2?family=Bebas+Neue&family=Oswald:wght@400;500&family=Roboto+Condensed:wght@400;700&family=Poiret+One&family=Crimson+Text&display=swap">
<style>
  :root {
    --purple-rule: #7a2f86;
    --header-pink: #c2407e;
    --header-violet: #5b2560;
    --header-lime: #d7e38a;
    --stage-dark: #151515;
    --stage-mid: #2b2b2b;
    --video-red: #b5231c;
    --video-deep: #3a1210;
    --video-teal: #1d5a4c;
    --accent-blue: #16a3e4;
    --panel: rgba(30, 30, 30, 0.88);
    --white: #ffffff;
    --nav-dim: #8c8c8c;
    --paper: #c9c9c9;
    --paper-text: #ffffff;
    --heading-dark: #333333;
  }
  * { box-sizing: border-box; margin: 0; padding: 0; }
  html, body { width: 1200px; height: 985px; overflow: hidden; background: var(--stage-dark); }
  .site { position: relative; width: 1200px; height: 985px; }

  /* Header */
  .masthead { position: absolute; left: 0; top: 0; width: 1200px; height: 253px;
    background: radial-gradient(ellipse at 55% 15%, var(--header-lime) 0%, rgba(215,227,138,0) 35%),
                linear-gradient(90deg, var(--header-pink) 0%, var(--header-violet) 45%, #6e2a6a 70%, #b34b9a 100%); }
  .masthead-rule { position: absolute; left: 0; top: 253px; width: 1200px; height: 4px; background: var(--purple-rule); }
  .brand { position: absolute; left: 0; width: 1200px; top: 108px; text-align: center;
    font-family: "Oswald", sans-serif; font-weight: 500; font-size: 44px; letter-spacing: 8px; color: var(--white); }
  .social { position: absolute; right: 16px; top: 203px; display: flex; gap: 14px; }
  .social a { display: flex; align-items: center; gap: 6px; color: var(--white); text-decoration: none;
    font-family: "Roboto Condensed", sans-serif; font-size: 13px; }
  .social .dot { width: 14px; height: 14px; border-radius: 50%; background: var(--white); }

  /* Stage */
  .stage { position: absolute; left: 0; top: 257px; width: 1200px; height: 515px;
    background: radial-gradient(ellipse at 50% 80%, var(--stage-mid) 0%, var(--stage-dark) 70%); }
  .nav { position: absolute; right: 30px; top: 270px; display: flex; gap: 45px;
    font-family: "Bebas Neue", sans-serif; font-size: 13px; letter-spacing: 3px; }
  .nav a { color: var(--nav-dim); text-decoration: none; padding-bottom: 3px; }
  .nav a.current { color: var(--white); border-bottom: 2px solid var(--purple-rule); }

  .player { position: absolute; left: 247px; top: 315px; width: 723px; height: 423px; overflow: hidden;
    background: linear-gradient(135deg, var(--video-teal) 0%, var(--video-red) 35%, #c23a30 65%, var(--video-deep) 100%); }
  .player-info { position: absolute; left: 16px; top: 16px; }
  .player-thumb { position: absolute; left: 0; top: 0; width: 73px; height: 73px; background: linear-gradient(#8a8f8f, #3e3e3e); }
  .player-title { position: absolute; left: 78px; top: 0; white-space: nowrap; background: var(--panel);
    padding: 6px 12px; font-family: "Roboto Condensed", sans-serif; font-weight: 700; font-size: 22px; color: var(--accent-blue); }
  .player-from { position: absolute; left: 78px; top: 44px; white-space: nowrap; background: var(--panel);
    padding: 4px 10px; font-family: "Roboto Condensed", sans-serif; font-size: 15px; color: var(--white); }
  .player-from span { color: var(--accent-blue); }
  .player-actions { position: absolute; right: 19px; top: 18px; display: flex; flex-direction: column; gap: 6px; }
  .action { width: 57px; height: 46px; border-radius: 5px; background: var(--panel); color: var(--white);
    display: flex; flex-direction: column; align-items: center; justify-content: center; gap: 2px;
    font-family: "Roboto Condensed", sans-serif; font-weight: 700; font-size: 11px; }
  .controls { position: absolute; left: 16px; bottom: 18px; right: 19px; height: 52px; }
  .play-btn { position: absolute; left: 0; top: 0; width: 92px; height: 52px; border-radius: 5px; background: var(--panel);
    display: flex; align-items: center; justify-content: center; }
  .bar { position: absolute; left: 100px; top: 12px; right: 0; height: 36px; border-radius: 4px; background: var(--panel); }
  .track { position: absolute; left: 15px; top: 13px; width: 446px; height: 11px; border: 1px solid #777; background: #2b2b2b; }
  .track .loaded { position: absolute; left: 0; top: 0; height: 100%; width: 64%; background: #666; }
  .track .played { position: absolute; left: 0; top: 0; height: 100%; width: 44%; background: var(--accent-blue); }
  .time { position: absolute; left: 188px; top: -22px; background: var(--white); color: #222; border-radius: 2px;
    padding: 1px 4px; font-family: "Roboto Condensed", sans-serif; font-size: 11px; }
  .bar-tools { position: absolute; right: 10px; top: 8px; display: flex; align-items: center; gap: 10px;
    font-family: "Roboto Condensed", sans-serif; font-weight: 700; font-style: italic; font-size: 16px; color: var(--accent-blue); }
  .volume { display: flex; gap: 2px; }
  .volume i { width: 3px; height: 14px; background: var(--accent-blue); }

  /* Lower panels */
  .lower { position: absolute; left: 0; top: 772px; width: 1200px; height: 213px; background: var(--paper); }
  .feature { position: absolute; top: 33px; }
  .feature-photo { position: absolute; left: 0; top: 0; width: 200px; height: 131px;
    background: linear-gradient(160deg, #9a9a9a 0%, #3a3a3a 45%, #0f0f0f 100%); box-shadow: 0 6px 8px rgba(0,0,0,0.35); }
  .feature-heading { position: absolute; left: 221px; top: -14px; white-space: nowrap; font-weight: 400;
    font-family: "Poiret One", sans-serif; font-size: 44px; color: var(--heading-dark); letter-spacing: -1px; }
  .feature-list { position: absolute; left: 218px; top: 48px; list-style: none; white-space: nowrap;
    font-family: "Crimson Text", serif; font-size: 13px; line-height: 20px; color: var(--paper-text); }
  .feature-list li::before { content: "\2022"; margin-right: 2px; }
  .news { left: 75px; }
  .events { left: 635px; }
</style>
</head>
<body>
<div class="site">
  <header class="masthead" role="img" aria-label="Crowd of clubbers with raised hands in pink and purple light"></header>
  <div class="masthead-rule"></div>
  <div class="brand">DJVORN</div>
  <nav class="social">
    <a href="#"><span class="dot"></span>Tunedrift</a>
    <a href="https://www.pagelinker.example/pages/DJ-Vorn/730162948415207"><span class="dot"></span>Pagelinker</a>
  </nav>

  <section class="stage" role="img" aria-label="Dim view of a DJ deck with crowd silhouettes"></section>
  <nav class="nav">
    <a href="#">HOME</a>
    <a href="#" class="current">NEWS</a>
    <a href="#">BOOKING</a>
  </nav>

  <div class="player" role="img" aria-label="Video still of a DJ performing under red stage lights">
    <div class="player-info">
      <div class="player-thumb" role="img" aria-label="Channel thumbnail"></div>
      <div class="player-title">DJVORN IN LOS ANGELES PT. 1</div>
      <div class="player-from">from <span>DJVorn Channel</span></div>
    </div>
    <div class="player-actions">
      <div class="action">
        <svg width="22" height="18" viewBox="0 0 22 18"><path d="M11 17 L2 8 A5 5 0 0 1 11 3 A5 5 0 0 1 20 8 Z" fill="#fff"/></svg>LIKE</div>
      <div class="action">
        <svg width="22" height="18" viewBox="0 0 22 18" fill="#fff"><rect x="2" y="12" width="4" height="4"/><rect x="9" y="7" width="4" height="4"/><rect x="16" y="2" width="4" height="4"/></svg>SHARE</div>
      <div class="action">
        <svg width="28" height="18" viewBox="0 0 28 18" fill="none" stroke="#fff" stroke-width="2.5"><path d="M8 3 L2 9 L8 15 M20 3 L26 9 L20 15 M16 2 L12 16"/></svg>EMBED</div>
    </div>
    <div class="controls">
      <div class="play-btn"><svg width="20" height="22" viewBox="0 0 20 22"><path d="M2 1 L19 11 L2 21 Z" fill="#fff"/></svg></div>
      <div class="bar">
        <div class="track"><div class="loaded"></div><div class="played"></div><div class="time">00:34</div></div>
        <div class="bar-tools">
          <span class="volume"><i></i><i></i><i></i><i></i><i></i><i></i><i></i><i></i><i></i><i></i></span>
          <span>HD</span>
          <svg width="16" height="16" viewBox="0 0 16 16" fill="none" stroke="#fff" stroke-width="2"><path d="M1 5 V1 H5 M11 1 H15 V5 M15 11 V15 H11 M5 15 H1 V11"/></svg>
        </div>
      </div>
    </div>
  </div>

  <section class="lower">
    <article class="feature news">
      <div class="feature-photo" role="img" aria-label="Black and white photo of a DJ at the decks"></div>
      <h2 class="feature-heading">latest news</h2>
      <ul class="feature-list">
        <li>Lorem Ipsum, London, 08 June 2013, Friday</li>
        <li>Lorem Ipsum, Australia, 23 April 2013, Sunday</li>
        <li>Lorem Ipsum, Hong Kong, 01 January 2013, Saturday</li>
        <li>Lorem Ipsum, Las Vegas, 13 August 2012, Wednesday</li>
        <li>Lorem Ipsum, Bangkok, 25 December 2011, Saturday</li>
      </ul>
    </article>
    <article class="feature events">
      <div class="feature-photo" role="img" aria-label="Black and white photo of a DJ with arms raised behind the decks"></div>
      <h2 class="feature-heading">upcoming events</h2>
      <ul class="feature-list">
        <li>Lorem Ipsum, London, 08 June 2013, Friday</li>
        <li>Lorem Ipsum, Australia, 23 April 2013, Sunday</li>
        <li>Lorem Ipsum, Hong Kong, 01 January 2013, Saturday</li>
        <li>Lorem Ipsum, Las Vegas, 13 August 2012, Wednesday</li>
        <li>Lorem Ipsum, Bangkok, 25 December 2011, Saturday</li>
      </ul>
    </article>
  </section>
</div>
</body>
</html>
```